Thornbeck Advisory Group Business Card Design Project

2-sided business card for my small (me and a couple subcontractors) firm, which consults to public community colleges and school districts and public agencies in California on energy matters, mostly solar electric systems that can reduce their electricity use by as much as 80%. I prepare requests for proposals (RFPs), manage the RFP processes, and work with the solar vendors to get the best deal for my clients. I also do regulatory and legislative advocacy for strong renewable energy policies. I do lots of quantitative analysis to make sure the solar systems are sized to produce the maximum monetary savings and focus a lot on the aesthetic design of the solar systems, as architectural features of the campuses (most are carport structures built in parking lots, but some are built on the ground and on rooftops). All my work is geared to getting the best value, highest quality, and most reliable solar system. My career background is in public interest energy advocacy; I'm not a consultant trying to make a million dollars but someone who is still serving in the public interest.

My competition is made up of much larger firms; this business card/logo in large part is intended to present an image of my firm as an equal to these larger firms despite my smaller size.

Essential information as follows:
Firm name: Thornbeck Advisory Group
Tagline: Clean Energy Procurement for the Public Sector
Name: Walter Pennick
email, 2 phone number, and address listed as well.

Target Market(s)

Public schools, community colleges, & public agencies.There is a wide range in the sophistication of these organizations.

Industry/Entity Type

Parking

Requirements
Must have
• - several rich colors, which can be either in the logo or in the background - the overall feeling of the card should reflect richness of color. I have uploaded some photos showing some colors that I like together. By rich I do not necessarily mean bright. I suppose bright colors in the logo could be supported with rich colors in the overall background of the card.
- professional, and powerful in an understated way (not kooky, cartoonish, or very playful)
- the logo must NOT be too representational of solar energy or the sun, but at the same time it would be good for the logo to be somewhat suggestive of this.

Nice to have
• -I like abstract and geometric images (with rich colts).
- A very subtle reference to schools/colleges/education would be great but it CANNOT be explicit; it would have to be faintly suggestive.
- In the logo I like the idea of abstract or geometric shapes intersecting with other in an interesting and suggestive way, conveying the multiple aspects of my practice (economics, data analysis, energy analysis, problem solving, managing collaborative processes, policy analysis)
- My work relates to environmental concerns, especially climate change. Working this into the logo in a subtle way could be good, but it's not a requirement.
- I like the idea that the logo/card feels serene.
- In designing the business card, I kind of like the idea of having the tag line as the first thing they read, then they see the firm name.

Should not have
• Not:
- humorous
- boring
- overly slick
- overly formal
- whimsical

```html
<!DOCTYPE html>
<html lang="en">
<head>
<meta charset="utf-8">
<title>Thornbeck Advisory Group – Business Card</title>
<link rel="stylesheet" href="https://fonts.googleapis.com/css2?family=Libre+Bodoni:wght@400;600&display=swap">
<style>
  :root {
    --page: #d8d8d8;
    --olive: #a8980c;
    --olive-light: #cfc46a;
    --lavender: #8f8ee8;
    --ink-blue: #2626e6;
    --panel-blue: #1010c0;
    --solar-yellow: #d6d21c;
    --solar-olive: #8a8412;
    --soft-white: #f4f2ff;
    --serif: "Libre Bodoni", "Bodoni Moda", Georgia, serif;
  }
  * { box-sizing: border-box; margin: 0; padding: 0; }
  html, body { width: 1200px; height: 655px; overflow: hidden; }
  body { background: var(--page); position: relative; font-family: var(--serif); }

  .card { position: absolute; width: 526px; height: 300px; overflow: hidden; }

  /* Front */
  .card-front {
    left: 46px; top: 97px;
    background: linear-gradient(180deg, var(--olive) 0%, #b8a93a 30%, #b6b3a6 55%, #a4a2de 75%, var(--lavender) 100%);
  }
  .card-front .waves { position: absolute; inset: 0; }
  .front-brand {
    position: absolute; left: 0; right: 0; top: 128px;
    display: flex; align-items: center; justify-content: center; gap: 10px;
  }
  .brand-mark { width: 12px; height: 12px; background: var(--ink-blue); }
  .front-brand .brand-name {
    font-size: 30px; font-weight: 600; color: var(--ink-blue); letter-spacing: 0.5px;
  }
  .tagline {
    position: absolute; left: 0; right: 0; top: 248px; text-align: center;
    font-size: 21px; color: var(--soft-white); letter-spacing: 0.3px;
    text-shadow: 1px 1px 2px rgba(40, 40, 80, 0.7);
  }

  /* Back */
  .card-back { left: 612px; top: 126px; background: #ffffff; }
  .card-back .shapes { position: absolute; inset: 0; }
  .contact { position: absolute; left: 52px; top: 18px; color: var(--ink-blue); }
  .contact .person-name { font-size: 28px; font-weight: 400; margin-bottom: 8px; }
  .contact .email { font-size: 17px; margin-bottom: 6px; }
  .contact .phone { font-size: 17px; line-height: 18px; }
  .back-brand {
    position: absolute; left: 380px; width: 140px; top: 78px; text-align: center;
    font-size: 15px; font-weight: 600; color: var(--solar-yellow); line-height: 1.2;
  }
  .address {
    position: absolute; left: 380px; width: 140px; top: 138px; text-align: center;
    font-size: 8px; color: #ffffff; line-height: 1.3;
  }
</style>
</head>
<body>

  <section class="card card-front">
    <svg class="waves" width="526" height="300" viewBox="0 0 526 300" aria-hidden="true">
      <path d="M120,0 C260,60 360,40 526,20 L526,0 Z" fill="#ffffff" opacity="0.12"/>
      <path d="M0,150 C140,110 260,150 380,110 C440,90 490,40 526,10 L526,300 L0,300 Z" fill="#ffffff" opacity="0.14"/>
      <path d="M0,200 C160,150 300,200 420,160 C470,145 505,120 526,100 L526,300 L0,300 Z" fill="#ffffff" opacity="0.14"/>
      <path d="M0,235 C180,200 320,230 526,170 L526,300 L0,300 Z" fill="#ffffff" opacity="0.1"/>
    </svg>
    <div class="front-brand">
      <span class="brand-mark"></span>
      <span class="brand-name">Thornbeck Advisory Group</span>
    </div>
    <p class="tagline">Clean Energy Procurement for the Public Sector</p>
  </section>

  <section class="card card-back">
    <svg class="shapes" width="526" height="300" viewBox="0 0 526 300">
      <defs>
        <linearGradient id="solarFill" x1="0" y1="0" x2="1" y2="1">
          <stop offset="0" stop-color="#e2de3a"/>
          <stop offset="0.5" stop-color="#c9c41a"/>
          <stop offset="1" stop-color="#8a8412"/>
        </linearGradient>
      </defs>
      <path d="M363,0 C320,70 300,210 250,300 L526,300 L526,0 Z" fill="var(--panel-blue)"/>
      <path role="img" aria-label="Solar panel array surface"
            d="M0,110 C70,135 160,190 270,186 C380,182 450,160 526,168 L526,300 L0,300 Z"
            fill="url(#solarFill)" opacity="0.92"/>
      <path d="M0,110 C70,135 160,190 270,186 C380,182 450,160 526,168"
            fill="none" stroke="#f0ec50" stroke-width="4"/>
    </svg>
    <div class="contact">
      <h1 class="person-name">Walter Pennick</h1>
      <p class="email">emailaddress@somewhere.com</p>
      <p class="phone">xxx-xxx-xxxx</p>
      <p class="phone">xxx-xxx-xxxx</p>
    </div>
    <p class="back-brand">Thornbeck Advisory Group</p>
    <p class="address">xxxx Street Address<br>Somewhere, GA xxxxx</p>
  </section>

</body>
</html>
```